A5 flyer required for alloy wheel refurbishment/window tinting company based in UK

Double sided flyer to promote our services. Company name is The Velquins. Design of the flyer to mirror our current website design (www.the-velquins.com). This flyer will be sent out to potential trade customers, so must be an informative layout, small amount of text, a good number of pictures showing our work. Our two main services are alloy wheel refurbishment and window tinting. Whilst we'd like the flyer to be informative we also want a fresh and funky design, something that will get noticed, something non-generic looking. Typical establishments that will be receiving this flyer are bodyshops, car dealerships, prestigious used car sales.

A funky and fresh design is of paramount importance, whilst remaining informative and uncluttered.

• Frames for up to 4 pictures
Opening hours
Address
Free collection and delivery service available

```html
<!DOCTYPE html>
<html lang="en">
<head>
<meta charset="utf-8">
<title>The Velquins – Alloy Wheel Refurbishment &amp; Window Tinting</title>
<link rel="stylesheet" href="https://fonts.googleapis.com/css2?family=Poppins:wght@400;600;700&display=swap">
<style>
  :root {
    --paper: #ffffff;
    --ink: #000000;
    --orange: #f7941d;
    --white: #ffffff;
    --rule: #5a5a5a;
    --photo-light: #bdbdbd;
    --photo-dark: #1b1b1b;
    --stripe-a: #2a2a2a;
    --stripe-b: #555555;
  }
  * { box-sizing: border-box; margin: 0; padding: 0; }
  html, body { width: 1200px; height: 900px; overflow: hidden; background: var(--paper); }
  body { position: relative; font-family: "Poppins", "Century Gothic", sans-serif; }

  .side { position: absolute; top: 32px; height: 823px; background: var(--ink); overflow: hidden; }
  .side--front { left: 18px; width: 579px; }
  .side--back { left: 601px; width: 584px; }

  .photo { position: absolute; }
  .photo--car-side { left: 0; top: 138px; width: 579px; height: 262px;
    background: linear-gradient(160deg, var(--photo-light) 0%, #9a9a9a 55%, #3d3d3d 100%); }
  .photo--wheel { left: 0; top: 400px; width: 579px; height: 423px;
    background: radial-gradient(circle at 38% 60%, #cfcfcf 0%, #8c8c8c 30%, #2a2a2a 62%, var(--photo-dark) 100%); }

  .brand { position: absolute; display: flex; align-items: center; gap: 8px;
    color: var(--orange); font-weight: 600; white-space: nowrap; }
  .brand__dot { width: 12px; height: 12px; border-radius: 50%; background: var(--orange); flex: none; }
  .brand--front { left: 316px; top: 52px; font-size: 30px; }
  .brand--back { left: 22px; top: 540px; font-size: 34px; }

  .headline { position: absolute; left: 18px; top: 26px; color: var(--orange);
    font-weight: 600; font-size: 88px; line-height: 133px; letter-spacing: 3px; white-space: nowrap; }

  .contact { position: absolute; left: 12px; top: 8px; color: var(--white); font-weight: 700; }
  .contact__email { font-size: 31px; line-height: 44px; }
  .contact__line { font-size: 39px; line-height: 46px; }

  .services { position: absolute; left: 10px; width: 564px; top: 155px; text-align: center;
    color: var(--orange); font-weight: 700; font-size: 18.5px; line-height: 27.5px; }

  .divider { position: absolute; left: 14px; width: 556px; top: 302px; height: 1px; background: var(--rule); }

  .stripes { position: absolute; left: 0; top: 0; width: 584px; height: 823px; }

  .pickup { position: absolute; left: 16px; top: 310px; color: var(--white); font-size: 21px; white-space: nowrap; }
  .pickup em { font-style: normal; color: var(--orange); }

  .gallery { position: absolute; left: 16px; top: 352px; display: flex; gap: 4px; }
  .gallery__frame { border: 3px solid var(--white); height: 152px; }
  .gallery__frame--coupe { width: 225px; background: linear-gradient(180deg, #cfd3d6 0%, #f2f2f2 45%, #5c5c5c 100%); }
  .gallery__frame--rim { width: 98px; background: radial-gradient(circle, #8a8a8a 0%, #2b2b2b 55%, #b8b8b8 100%); }
  .gallery__frame--suv { width: 226px; background: linear-gradient(135deg, #4a4a4a 0%, #c9c9c9 50%, #6a6a6a 100%); }

  .address { position: absolute; left: 22px; top: 590px; color: var(--white); }
  .address__title { font-size: 31px; line-height: 38px; }
  .address__lines { font-size: 18.5px; line-height: 25px; padding-left: 6px; }
</style>
</head>
<body>
  <section class="side side--front">
    <div class="photo photo--car-side" role="img" aria-label="Photo of a silver sports car side panel and rear wheel arch"></div>
    <div class="photo photo--wheel" role="img" aria-label="Close-up photo of a refurbished multi-spoke silver alloy wheel on a black car"></div>
    <div class="brand brand--front"><span class="brand__dot"></span>The Velquins</div>
    <h1 class="headline">Alloy<br>Wheel<br>Refurb-<br>ishment &amp;<br>Window<br>Tinting</h1>
  </section>

  <section class="side side--back">
    <svg class="stripes" viewBox="0 0 584 823" role="img" aria-label="Diagonal striped background band">
      <defs>
        <linearGradient id="stripe-fill" x1="0" y1="0" x2="1" y2="1">
          <stop offset="0" stop-color="#555555"/>
          <stop offset="1" stop-color="#2a2a2a"/>
        </linearGradient>
      </defs>
      <polygon points="584,312 584,823 144,823" fill="url(#stripe-fill)"/>
    </svg>

    <div class="contact">
      <p class="contact__email">Email: info@the-velquins.com</p>
      <p class="contact__line">Tel: 01632 570010</p>
      <p class="contact__line">Fax: 01632 613002</p>
    </div>

    <p class="services">- Speaker upgrades - Media player integration - Sub and amp packages - Rear headrest screens and DVD players - Games console installation i.e. Playbox 3, Gamestack 360 - Reverse parking sensors - Handsfree bluetooth kits</p>

    <div class="divider"></div>

    <p class="pickup">Free <em>collection and delivery service</em> available</p>

    <div class="gallery">
      <div class="gallery__frame gallery__frame--coupe" role="img" aria-label="Photo of a white sports coupe with black alloy wheels"></div>
      <div class="gallery__frame gallery__frame--rim" role="img" aria-label="Photo of a black and silver refurbished alloy wheel"></div>
      <div class="gallery__frame gallery__frame--suv" role="img" aria-label="Photo of a silver alloy wheel on a dark SUV"></div>
    </div>

    <div class="brand brand--back"><span class="brand__dot"></span>The Velquins</div>

    <div class="address">
      <p class="address__title">Address:</p>
      <p class="address__lines">The Velquins<br>214 Kestrel Avenue Slough<br>Berkshire SL0 9QX</p>
    </div>
  </section>
</body>
</html>
```